Security Warning Sign

We have an existing sign that needs an update. I have attached a picture of the current square sign. We need to maintain the same wording. It needs to be professional and appropriate to attach to our customers fence. Also attached is a copy of our building sign which may lend some inspiration and hopefully the ai format will assist. The final sign will be 600mm x 600mmOur website is www.halvorngate.com.au

```html
<!DOCTYPE html>
<html lang="en">
<head>
<meta charset="utf-8">
<title>Security Warning Sign</title>
<link href="https://fonts.googleapis.com/css2?family=Open+Sans:wght@700;800&display=swap" rel="stylesheet">
<style>
  :root {
    --backdrop: #9b9d9e;
    --orange: #ee7f1f;
    --charcoal: #2a2928;
    --ink: #262626;
    --white: #ffffff;
    --panel-light: #f1f2f3;
    --panel-mid: #d4d5d7;
  }
  html, body {
    margin: 0;
    padding: 0;
    width: 1200px;
    height: 1170px;
    overflow: hidden;
    background: var(--backdrop);
    font-family: "Open Sans", Arial, sans-serif;
  }
  .sign {
    position: absolute;
    left: 232px;
    top: 217px;
    width: 735px;
    height: 735px;
    display: flex;
    flex-direction: column;
  }
  .sign-header {
    height: 140px;
    background: var(--orange);
    display: flex;
    align-items: center;
    justify-content: center;
  }
  .sign-title {
    margin: 0;
    font-size: 106px;
    font-weight: 800;
    letter-spacing: 2px;
    line-height: 1;
    color: var(--white);
    -webkit-text-stroke: 3px var(--charcoal);
    paint-order: stroke fill;
    text-shadow: 0 0 0 var(--white), 2px 2px 0 var(--white), -2px -2px 0 var(--white), 2px -2px 0 var(--white), -2px 2px 0 var(--white);
  }
  .sign-body {
    position: relative;
    height: 473px;
    display: flex;
    align-items: center;
    justify-content: center;
  }
  .body-texture {
    position: absolute;
    inset: 0;
    background: linear-gradient(135deg, var(--panel-mid) 0%, var(--panel-light) 45%, var(--panel-mid) 75%, var(--panel-light) 100%);
  }
  .notice {
    position: relative;
    margin: 0;
    text-align: center;
    font-size: 66px;
    font-weight: 800;
    line-height: 86px;
    color: var(--ink);
    letter-spacing: 0.5px;
  }
  .sign-footer {
    height: 122px;
    background: var(--charcoal);
    display: flex;
    align-items: center;
    padding: 0 26px;
    box-sizing: border-box;
  }
  .brand {
    display: flex;
    align-items: center;
    gap: 12px;
    width: 288px;
  }
  .brand-dot {
    width: 70px;
    height: 70px;
    border-radius: 50%;
    background: var(--orange);
    flex: none;
  }
  .brand-name {
    color: var(--white);
    font-weight: 800;
    font-size: 20px;
    line-height: 25px;
  }
  .contact {
    font-weight: 800;
    font-size: 24px;
    line-height: 25px;
    color: var(--white);
  }
  .contact-phone { color: var(--orange); }
</style>
</head>
<body>
  <section class="sign">
    <header class="sign-header">
      <h1 class="sign-title">WARNING</h1>
    </header>
    <div class="sign-body">
      <div class="body-texture" role="img" aria-label="Faint light-grey low-poly geometric background pattern"></div>
      <p class="notice">ELECTRONIC<br>SURVEILLANCE<br>AND RECORDING<br>DEVICES INSTALLED<br>IN THIS AREA</p>
    </div>
    <footer class="sign-footer">
      <div class="brand">
        <span class="brand-dot"></span>
        <span class="brand-name">HALVORNGATE<br>SECURITY<br>SERVICES</span>
      </div>
      <div class="contact">
        <div class="contact-name">HALVORNGATE SECURITY</div>
        <div class="contact-phone">1300 555 014</div>
        <div class="contact-web">www.halvorngate.com.au</div>
      </div>
    </footer>
  </section>
</body>
</html>
```